Can I be me speaking engagement

the flyer is about a speaking engagement for women's groups. Flyer should be simple, soft, engaging, clean and professional. I am a life coach and also a talk show host. the event I will be advertising is for groups of women. It will be given to church groups, female clubs and organizations. The name of my company is Marlow Pathfinder Life Coaching Institute.

Target Market(s)

professional women over thirty years old

Font styles to use
Script

Colors
ffffff
34a7d8
85cae6

Requirements
Must have
• use my photo and logo only
Should not have
• anything distracting

```html
<!DOCTYPE html>
<html lang="en">
<head>
<meta charset="utf-8">
<title>Can I Be Me – Speaking Engagement Flyer</title>
<link rel="stylesheet" href="https://fonts.googleapis.com/css2?family=Kaushan+Script&family=Lobster&family=Lato:wght@400;700&display=swap">
<style>
  :root {
    --white: #ffffff;
    --sky: #34a7d8;
    --sky-soft: #85cae6;
    --sky-deep: #1a8fcf;
    --ink: #333a40;
    --page: #e9ecef;
    --suit: #2e4468;
    --photo-light: #dfe6ea;
  }
  * { box-sizing: border-box; margin: 0; padding: 0; }
  html, body { width: 1200px; height: 1200px; overflow: hidden; background: var(--page); }
  .flyer {
    position: absolute; left: 140px; top: 5px;
    width: 920px; height: 1190px;
    background: var(--white); overflow: hidden;
    box-shadow: 0 2px 10px rgba(0,0,0,.12);
  }
  .speaker-photo {
    position: absolute; left: 300px; top: 0; width: 620px; height: 1190px;
    background:
      radial-gradient(ellipse 230px 300px at 370px 330px, #8a5a3c 0%, #6b4129 60%, rgba(107,65,41,0) 100%),
      linear-gradient(180deg, rgba(255,255,255,0) 0%, rgba(255,255,255,0) 40%, var(--suit) 62%, #243657 100%),
      linear-gradient(90deg, var(--white) 0%, var(--photo-light) 35%, #cfd9df 100%);
    -webkit-mask-image: linear-gradient(90deg, transparent 0%, #000 30%);
            mask-image: linear-gradient(90deg, transparent 0%, #000 30%);
  }
  .headline {
    position: absolute; left: 42px; top: 38px;
    font-family: "Kaushan Script", cursive;
    color: var(--sky); font-size: 58px; line-height: 80px;
  }
  .coach-name {
    position: absolute; left: 44px; top: 198px;
    font-family: "Lobster", cursive;
    color: var(--ink); font-size: 72px; line-height: 88px;
  }
  .session-blurb {
    position: absolute; left: 42px; top: 403px; width: 340px;
    font-family: "Lato", sans-serif; font-size: 29px; line-height: 37.8px;
    color: var(--ink);
  }
  .portrait {
    position: absolute; left: 25px; top: 845px; width: 330px; height: 330px;
    border-radius: 50%; border: 8px solid var(--sky-soft);
    background:
      radial-gradient(circle at 50% 22%, #2b2420 0 26%, transparent 27%),
      radial-gradient(ellipse 60% 40% at 45% 95%, #2c5fae 0 100%, transparent 100%),
      linear-gradient(160deg, #e9e6e2, #d9d3cc);
    z-index: 2;
  }
  .invite-band {
    position: absolute; left: 340px; top: 926px; width: 580px; height: 87px;
    background: var(--sky-deep); color: var(--white);
    font-family: Arial, "Helvetica Neue", sans-serif; font-weight: 700;
    font-size: 21px; line-height: 27px; padding: 20px 0 0 32px;
  }
  .contact-band {
    position: absolute; left: 320px; top: 1023px; width: 600px; height: 87px;
    background: var(--sky-soft); color: var(--ink);
    font-family: "Lato", sans-serif; padding: 7px 0 0 52px;
  }
  .contact-label { font-size: 25px; line-height: 30px; }
  .contact-phone { font-size: 38px; line-height: 44px; font-weight: 700; color: #2b2f33; }
</style>
</head>
<body>
  <main class="flyer">
    <div class="speaker-photo" role="img" aria-label="Photo of the life coach, smiling in a navy suit with arms crossed, soft blurred background"></div>

    <h1 class="headline">A heart to heart<br>conversation with</h1>
    <h2 class="coach-name">Life Coach<br>Renna Calloway</h2>

    <p class="session-blurb">Can I be me is an interactive soul searching session that will help women share their stories and be real about the things that matter most.</p>

    <div class="portrait" role="img" aria-label="Circular portrait photo of the host in a blue blouse"></div>

    <div class="invite-band">TO INVITE RENNA TO YOUR WOMEN'S GROUP<br>OR GATHERING.</div>
    <div class="contact-band">
      <div class="contact-label">CONTACT US AT</div>
      <div class="contact-phone">242-555-0143 or 555-0198</div>
    </div>
  </main>
</body>
</html>
```